Football tournament flyer

I would like a quick turn around for this please.
I need a flyer to promote an 11 aside football tournament I am organising to celebrate the 23rd independence of my country Somaliland. Please use the national colours of our flag in the flyer, I have attached a file for your consideration.
The tournament will take place on 10/05/2014, from 9am - 8pm. The venue will be Corvell Open Space, Tresham Lane, Enfield, EN7 2QJ.
Refreshments, food and entertainment will be provided.
The name of the cup is Warsadeq Cup.
Spaces are limited and the entry fee per team is £200. All proceeds are for charity projects in Somaliland.
To register a team contact Bashir Yusuf on 07591 248 613 or Warsame Hirsi on 07462 571 380.
The best players will have the opportunity to represent Somaliland in an international game on the 17/05/2014.
The tournament is organised by Dalmar FC and Kindwell Foundation.
Industry/Entity Type
Entertainment

```html
<!DOCTYPE html>
<html lang="en">
<head>
<meta charset="utf-8">
<title>Warsadeq Cup – Football Tournament Flyer</title>
<link rel="stylesheet" href="https://fonts.googleapis.com/css2?family=Oswald:wght@500;700&family=Roboto+Condensed:ital,wght@0,400;0,700;1,700&display=swap">
<style>
  :root {
    --night: #05070d;
    --deep-blue: #0b1a3a;
    --flare: #d8232a;
    --gold-light: #fbf0c8;
    --gold: #e6c878;
    --gold-dark: #b88a3a;
    --grass-dark: #0f3b13;
    --grass: #2f7d26;
    --white: #ffffff;
    --mint: #d6f0c8;
    --ink: #1b1b1b;
    --flag-green: #0b8a3c;
    --flag-red: #d2202a;
  }
  * { margin: 0; padding: 0; box-sizing: border-box; }
  html, body { width: 849px; height: 1200px; overflow: hidden; background: var(--night); }
  .flyer {
    position: relative; width: 849px; height: 1200px; overflow: hidden;
    background: linear-gradient(180deg, var(--night) 0%, var(--deep-blue) 38%, #08121f 56%, var(--grass-dark) 62%, var(--grass) 85%, var(--grass-dark) 100%);
    font-family: "Roboto Condensed", Arial, sans-serif; color: var(--white);
  }
  .hero-art {
    position: absolute; left: 0; top: 0; width: 849px; height: 420px;
    background:
      radial-gradient(ellipse 260px 150px at 330px 140px, rgba(255,120,60,.85), rgba(216,35,42,.35) 50%, transparent 75%),
      radial-gradient(ellipse 260px 260px at 640px 230px, rgba(90,140,220,.45), transparent 70%),
      linear-gradient(180deg, #02040a, #0c1d40);
  }
  .flag {
    position: absolute; top: 30px; right: 30px; width: 150px; height: 92px;
    display: flex; flex-direction: column; box-shadow: 0 2px 6px rgba(0,0,0,.5);
  }
  .flag span { flex: 1; }
  .flag .band-green { background: var(--flag-green); }
  .flag .band-white { background: var(--white); display: flex; align-items: center; justify-content: center; }
  .flag .band-red { background: var(--flag-red); }
  .event-time {
    position: absolute; left: 70px; top: 275px;
    font-family: "Oswald", Arial, sans-serif; font-weight: 700; line-height: 1;
    text-shadow: 0 2px 6px rgba(0,0,0,.7);
  }
  .event-time .date { font-size: 62px; }
  .event-time .hours { font-size: 62px; margin-top: 6px; }
  .cup-title {
    position: absolute; left: 0; width: 100%; text-align: center;
    font-family: "Oswald", Arial, sans-serif; font-weight: 700; line-height: 1;
    background: linear-gradient(180deg, var(--gold-light) 0%, var(--gold) 55%, var(--gold-dark) 100%);
    -webkit-background-clip: text; background-clip: text; color: transparent;
  }
  .cup-title.name { top: 408px; font-size: 150px; letter-spacing: 2px; }
  .cup-title.cup { top: 560px; font-size: 150px; letter-spacing: 4px; }
  .info { position: absolute; font-size: 22px; line-height: 1.2; }
  .info strong { font-weight: 700; text-transform: uppercase; }
  .info.entry { left: 58px; top: 575px; width: 230px; }
  .info.selection { right: 40px; top: 575px; width: 250px; }
  .note { position: absolute; font-size: 20px; line-height: 1.2; color: var(--mint); font-weight: 700; }
  .note.refreshments { left: 80px; top: 775px; width: 210px; }
  .note.organisers { right: 50px; top: 775px; width: 250px; }
  .trophy {
    position: absolute; left: 325px; top: 755px; width: 200px; height: 310px;
    background: radial-gradient(ellipse 80px 110px at 100px 110px, #f1d28a, #a8782e 70%, transparent 72%),
                radial-gradient(circle 62px at 100px 240px, #f5f5f5, #9a9a9a 80%, transparent 82%);
  }
  .contact-line { position: absolute; font-size: 24px; font-style: italic; font-weight: 700; color: var(--mint); }
  .contact-line.first { left: 60px; top: 910px; }
  .contact-line.second { right: 60px; top: 910px; }
  .phone {
    position: absolute; top: 945px; font-family: "Oswald", Arial, sans-serif; font-weight: 700;
    font-size: 52px; text-shadow: 0 2px 6px rgba(0,0,0,.6);
  }
  .phone.first { left: 60px; }
  .phone.second { right: 60px; }
  .venue {
    position: absolute; left: 0; bottom: 0; width: 100%; height: 105px;
    background: var(--white); color: var(--ink);
    display: flex; align-items: center; justify-content: center;
    font-family: "Roboto Condensed", Arial, sans-serif; font-weight: 700; font-size: 38px;
  }
</style>
</head>
<body>
<main class="flyer">
  <div class="hero-art" role="img" aria-label="Footballer striking a blazing football against a dark night sky"></div>

  <div class="flag" role="img" aria-label="Somaliland flag">
    <span class="band-green"></span>
    <span class="band-white">
      <svg width="26" height="26" viewBox="0 0 24 24"><polygon points="12,1 15,9 23,9 16.5,14 19,22 12,17 5,22 7.5,14 1,9 9,9" fill="#000"/></svg>
    </span>
    <span class="band-red"></span>
  </div>

  <div class="event-time">
    <p class="date">10/05/2014</p>
    <p class="hours">9am - 8pm</p>
  </div>

  <h1 class="cup-title name">WARSADEQ</h1>
  <p class="cup-title cup">CUP</p>

  <p class="info entry"><strong>Spaces are limited and the entry fee per team is £200.</strong> All proceeds are for charity projects in Somaliland.</p>
  <p class="info selection">The best players will have the opportunity to represent Somaliland in an international game on the 17/05/2014.</p>

  <p class="note refreshments">Refreshments, food and entertainment will be provided.</p>
  <p class="note organisers">The tournament is organised by Dalmar FC and Kindwell Foundation.</p>

  <div class="trophy" role="img" aria-label="Gold trophy cup resting on a football"></div>

  <p class="contact-line first">To register a team contact Bashir Yusuf on:</p>
  <p class="contact-line second">or Warsame Hirsi on</p>
  <p class="phone first">07591 248 613</p>
  <p class="phone second">07462 571 380</p>

  <footer class="venue">Corvell Open Space, Tresham Lane, Enfield, EN7 2QJ.</footer>
</main>
</body>
</html>
```